Velvet Heron Website

We need a website for our software / project management services company based in South Africa called "Velvet Heron". We provide professional services to high value clients in the public and private sectors.

The website must present a highly professional company that exudes quality and confidence.

The theme should be a highly professional subdued look with a fairly limited palette. The neutral tone should be slightly offset with the colours from the company logo. The website should not look dead though, and subtle colour highligting should provide a fresh vibrant feel.

Refer to the current website for general content (www.velvetheron-example.co.za) that may be used. We would also like to make use of social integration and google maps.
Updates

Thanks to all the designers that have participated so far and to those that are cooking something up at this very minute :-)

We have received a lot of designs with elements that we absolutely love. So now the hard work of refining these designs can begin.

We'll try and provide feedback on every design received so far ... and await the beautiful designs that we haven't received yet :-)

Good Luck!

Reason: After careful consideration we are extending the deadline to make small revisions to some of the designs and to select the top three designs. Thank you for everyone who has made a contribution so far - we have several designs that we like and selecting the best one is proving to be difficult :-)

Target Market(s)

The company deals mostly with other businesses, so mostly B2B.

Industry/Entity Type

Software

Requirements
Nice to have
• Social integration

```html
<!DOCTYPE html>
<html lang="en">
<head>
<meta charset="utf-8">
<title>Velvet Heron</title>
<link rel="stylesheet" href="https://fonts.googleapis.com/css2?family=Arimo:wght@400;700&display=swap">
<style>
:root{
  --green:#86b630;
  --green-dark:#6f9b26;
  --nav-top:#a3cd57;
  --nav-bottom:#76a42f;
  --ink:#1c1c1c;
  --body:#666;
  --link:#333;
  --panel:#f1f1f1;
  --tweet:#efefef;
  --footer:#6e6e6e;
  --footer-text:#f2f2f2;
  --rule:#e2e2e2;
}
*{box-sizing:border-box;margin:0;padding:0}
html,body{width:945px;height:1200px;overflow:hidden}
body{position:relative;background:#fff;font-family:"Arimo",Arial,sans-serif;color:var(--body)}
.abs{position:absolute}
a{color:var(--link);text-decoration:underline}
.green-link{color:var(--green)}
.hero-bg{left:0;top:0;width:945px;height:470px;background:linear-gradient(#fff 0,#fafafa 60%,#ececec 88%,#fff 100%)}
.hero-band{left:0;top:397px;width:945px;height:65px;background:linear-gradient(#e3e3e3,#f7f7f7 80%,#fff)}
.nav{left:34px;top:0;width:877px;height:37px;display:flex;background:linear-gradient(var(--nav-top),var(--nav-bottom));border-radius:0 0 4px 4px}
.nav a{flex:1;color:#fff;text-decoration:none;font-size:10.5px;letter-spacing:.4px;display:flex;align-items:center;justify-content:center;border-right:1px solid rgba(255,255,255,.35)}
.nav a:last-child{border-right:none}
.brand{left:62px;top:78px;display:flex;align-items:center;gap:12px}
.brand-mark{width:40px;height:40px;border-radius:50%;background:var(--green)}
.brand-name{font-size:40px;font-weight:700;color:#555;letter-spacing:-.5px}
.tagline{left:64px;top:172px;width:380px;font-size:19px;line-height:26px;color:var(--ink)}
.tagline span{color:var(--green)}
.learn-more{left:62px;top:299px;width:184px;height:37px;border-radius:3px;background:linear-gradient(#8a8a8a,#575757);color:#fff;font-size:17px;font-weight:700;padding:6px 12px;text-decoration:none;border:1px solid #555}
.dots{left:61px;top:355px;display:flex;gap:6px}
.dots i{width:13px;height:13px;border-radius:50%;border:1.5px solid #999;display:block}
.dots i.on{background:var(--green);border-color:#999}
.devices{left:482px;top:112px;width:428px;height:330px;border-radius:10px;background:linear-gradient(135deg,#3a3a3a,#cfcfcf 55%,#1f3c63)}
h2{font-weight:400;color:var(--green);font-size:19.5px}
.welcome{left:62px;top:462px;width:380px}
.lead{font-size:14.5px;line-height:21px;color:var(--ink);margin:10px 0 7px}
.copy{font-size:11px;line-height:17.5px}
.link-list{list-style:none;font-size:11px}
.link-list li{margin-top:13px}
.vr{width:1px;background:var(--rule)}
.projects{left:505px;top:462px}
.tweets{left:727px;top:462px;width:184px}
.tweet{background:var(--tweet);height:58px;margin-top:7px;padding:6px 11px;font-size:9.5px;line-height:16px;color:#555}
.tweet:first-of-type{margin-top:10px}
.tweet b{font-weight:400;color:var(--green)}
.social{left:764px;top:966px;display:flex;gap:10px;padding:6px 0 0 4px;border-top:1px solid #ddd;width:145px}
.social i{width:18px;height:18px;background:#8b8b8b;display:block;border-radius:2px}
.social i:first-child{background:#5aa9df}
.panel{left:34px;top:718px;width:660px;height:270px;background:var(--panel)}
.news{left:62px;top:739px;width:380px}
.news-photo{left:62px;top:774px;width:50px;height:73px;background:linear-gradient(#cfd6dd,#59606a)}
.like{left:62px;top:857px;width:39px;height:17px;border:1px solid #bbb;background:#fff;font-size:8.5px;color:#3b5998;padding:3px 0 0 16px;border-radius:2px}
.news-body{left:147px;top:769px;width:275px}
.news-body .lead{margin-top:0;font-size:14.5px}
.downloads{left:505px;top:739px}
.footer{left:0;top:1036px;width:945px;height:164px;background:var(--footer);color:var(--footer-text)}
.footer h3{font-weight:400;font-size:12.5px;color:#ddd}
.footer a{color:#fff}
.fcol{top:24px;font-size:9.5px;line-height:14.5px}
.footer-brand{left:508px;top:118px;display:flex;align-items:center;gap:6px;font-weight:700;font-size:14px;color:#bbb}
.footer-brand i{width:14px;height:14px;border-radius:50%;background:#999;display:block}
</style>
</head>
<body>
<div class="abs hero-bg"></div>
<div class="abs hero-band"></div>

<nav class="abs nav">
  <a href="#">COMPANY</a><a href="#">PROFESSIONAL SERVICES</a><a href="#">PORTFOLIO</a><a href="#">CONTACT</a>
</nav>

<div class="abs brand"><span class="brand-mark"></span><span class="brand-name">Velvet Heron</span></div>
<p class="abs tagline"><span>Velvet Heron</span> is a premium ICT solutions provider which delivers quality software development support services to clients in all sectors of industry.</p>
<a class="abs learn-more" href="#">Learn more</a>
<div class="abs dots"><i class="on"></i><i></i><i></i><i></i><i></i></div>
<div class="abs devices" role="img" aria-label="Desktop monitor, tablet and phone showing software screens with a classic car"></div>

<section class="abs welcome">
  <h2>Welcome</h2>
  <p class="lead">We provide professional services to high value clients in the public and private sectors.</p>
  <p class="copy">Lorem ipsum ad his scripta blandit partiendo, eum fastidii accumsan euripidis in, eum liber hendrerit an. Qui ut wisi vocibus suscipiantur, quo dicit ridens inciderint id. Quo mundi lobortis reformidans eu, legimus senserit definiebas an eos. Eu sit tincidunt incorrupte definitionem, vis mutat affert percipit cu, eirmod consectetuer signiferumque eu per. In usu latine equidem dolores.</p>
  <ul class="link-list" style="margin-top:8px">
    <li><a class="green-link" href="#">Check out our other services</a></li>
    <li><a class="green-link" href="#">Join our mailing list now</a></li>
  </ul>
</section>
<div class="abs vr" style="left:473px;top:462px;height:232px"></div>
<div class="abs vr" style="left:34px;top:462px;height:232px"></div>

<section class="abs projects">
  <h2>Recent proyects</h2>
  <ul class="link-list" style="margin-top:2px">
    <li><a href="#">Norvale Group</a></li>
    <li><a href="#">Quillsoft</a></li>
    <li><a href="#">BRANDT INDUSTRIES</a></li>
    <li><a href="#">Ostrava Bank</a></li>
    <li><a href="#">Harbour Street Ledger</a></li>
    <li><a class="green-link" href="#">See all our proyects</a></li>
  </ul>
</section>
<div class="abs vr" style="left:694px;top:462px;height:232px"></div>

<section class="abs tweets">
  <h2>Latest tweets</h2>
  <div class="tweet"><b>@velvetheron</b> Lorem ipsum ad his scripta blandit partiendo, eum fastidii accumsan euripidis in</div>
  <div class="tweet"><b>@velvetheron</b> Lorem ipsum ad his scripta blandit partiendo, eum fastidii accumsan euripidis in</div>
  <div class="tweet"><b>@velvetheron</b> Lorem ipsum ad his scripta blandit partiendo, eum fastidii accumsan euripidis in</div>
  <div class="tweet"><b>@velvetheron</b> Lorem ipsum ad his scripta blandit partiendo, eum fastidii accumsan euripidis in</div>
  <div class="tweet"><b>@velvetheron</b> Lorem ipsum ad his scripta blandit partiendo, eum fastidii accumsan euripidis in</div>
  <div class="tweet"><b>@velvetheron</b> Lorem ipsum ad his scripta blandit partiendo, eum fastidii accumsan euripidis in</div>
  <div class="tweet"><b>@velvetheron</b> Lorem ipsum ad his scripta blandit partiendo, eum fastidii accumsan euripidis in</div>
  <p style="font-size:11px;margin:12px 0 0 2px"><a class="green-link" href="#">Visit our tweeter site</a></p>
</section>
<div class="abs social" aria-label="Social links"><i></i><i></i><i></i></div>

<div class="abs panel"></div>
<section class="abs news"><h2>Latest news</h2></section>
<div class="abs news-photo" role="img" aria-label="Photo of business people shaking hands"></div>
<div class="abs like">Like</div>
<section class="abs news-body">
  <p class="lead">Development support services help to keep low costs in big industries: Cape Daily Courier</p>
  <p class="copy">Lorem ipsum ad his scripta blandit partiendo, eum fastidii accumsan euripidis in, eum liber hendrerit an. Qui ut wisi vocibus suscipiantur, quo dicit ridens inciderint id. Quo mundi lobortis reformidans eu, legimus senserit definiebas an eos. Eu sit tincidunt incorrupte definitionem.</p>
  <ul class="link-list" style="margin-top:8px">
    <li><a class="green-link" href="#">Read full story</a></li>
    <li><a class="green-link" href="#">Check all the news</a></li>
  </ul>
</section>
<div class="abs vr" style="left:473px;top:739px;height:232px"></div>
<section class="abs downloads">
  <h2>Downloads</h2>
  <ul class="link-list" style="margin-top:2px">
    <li><a href="#">Professional Graphics Trial</a></li>
    <li><a href="#">Virtual Desktop Demo</a></li>
    <li><a href="#">MSG Optimizer Demo</a></li>
    <li><a href="#">Phone photo viewer Demo</a></li>
    <li><a href="#">Tablet switcher Demo</a></li>
    <li><a class="green-link" href="#">See all our downloads</a></li>
  </ul>
</section>

<footer class="abs footer">
  <div class="abs fcol" style="left:63px">
    <h3>Recommended sites</h3>
    <ul class="link-list" style="font-size:9.5px;margin-top:4px">
      <li><a href="#">The development vault</a></li>
      <li><a href="#">Learnhall.example</a></li>
      <li><a href="#">scriptkit projects</a></li>
    </ul>
  </div>
  <div class="abs fcol" style="left:285px;width:180px">
    <h3>Suggestions?</h3>
    <p style="margin-top:13px">If you have any suggestions for this site or our work, please, feel free to contact us to <a href="#">suggestions@velvetheron-example.co.za</a> and help us to serve you better</p>
  </div>
  <div class="abs fcol" style="left:506px;width:400px">
    <h3>About this site</h3>
    <p style="margin-top:13px">Eum hinc argumentum te, no sit percipit adversarium, ne qui feugiat persecuti. Odio omnes scripserit ad est, ut vidit lorem maiestatis his, putent mandamus gloriatur ne pro. Oratio iriure rationibus ne his, ad est corrumpit splendide. Ad duo appareat moderatius, ei falli tollit denique eos.</p>
  </div>
  <div class="abs footer-brand"><i></i>Velvet Heron</div>
</footer>
</body>
</html>
```